Scientific project description

Here is a project description related to cellular mechanics, showing above the forces acting on cells in the tissues of our body. The forces on single cells are there to depict how forces are acting on cells (pressure squeezes the cell, shear flow is pushing the upward parts of the cell, tension pulls one part of the cell, strain is stretching the whole cell; the single cell images are to be found also on the last page). Intense red/purple are used to indicate that the forces are stressful (the colors to be used do not need to be exactly like these colors). The picture in the middle is a view of cells (same picture on next page if that needs to be modified). At the left, a description of what happens when everything is going well, i.e. the body stays healthy. At the right, if you dysfunction you get disease. Green nuances were used to indicate health, brownish, perhaps not so pleasant nuances were used to indicate disease. Below are the steps of the project.

On the whole, we're rather happy with the concept description as such, but it should look a little bit nicer. To many color nuances give a "noisy" impression, fonts could be nicer, layout more crisp, and the text on the steps should be more readable. We would also like to have two versions of the same picture, one with black background, one with white.

Target Market(s)

Scientists that are evaluating our project

Requirements
Must have
• Easy to grasp the idea, easy to read and understand the underlying idea.
Nice to have
• Would be good to have the Concept title ("Vorlint Concept and Envisioned Project Progression) on top of the figure as indicated in the second brief picture submitted.

```html
<!DOCTYPE html>
<html lang="en">
<head>
<meta charset="utf-8">
<title>Vorlint Concept and Envisioned Project Progression</title>
<link rel="stylesheet" href="https://fonts.googleapis.com/css2?family=Open+Sans:wght@600;700&display=swap">
<style>
  :root {
    --page: #ffffff;
    --panel: #000000;
    --ink-light: #ffffff;
    --ink-step: #1c2633;
  }
  html, body {
    margin: 0;
    width: 1200px;
    height: 1200px;
    overflow: hidden;
    background: var(--page);
  }
  .concept-sheet {
    display: block;
    width: 1200px;
    height: 1200px;
    font-family: "Open Sans", "Segoe UI", sans-serif;
  }
  .theme-colour {
    --wedge: #3a1416;
    --forces-band: #2e1213;
    --fitness: #3f8d3c;
    --fitness-low: #357a33;
    --frailty: #c65327;
    --frailty-low: #b14620;
    --step: #2aa6de;
    --step-top: #1c8fc6;
    --photo: url(#cellViewColour);
    --icon-area: rgba(255,255,255,0.08);
  }
  .theme-mono {
    --wedge: #474747;
    --forces-band: #171717;
    --fitness: #6e6e6e;
    --fitness-low: #626262;
    --frailty: #6e6e6e;
    --frailty-low: #626262;
    --step: #a3a3a3;
    --step-top: #8a8a8a;
    --photo: url(#cellViewMono);
    --icon-area: rgba(255,255,255,0.08);
  }
  .panel-bg { fill: var(--panel); }
  .title { fill: var(--ink-light); font-size: 38px; font-weight: 700; text-anchor: middle; }
  .force-wedge { fill: var(--wedge); }
  .force-icon { fill: var(--icon-area); }
  .force-label { fill: var(--ink-light); font-size: 25px; font-weight: 600; text-anchor: middle; }
  .pointer { fill: var(--ink-light); }
  .cell-view { fill: var(--photo); }
  .mechanostasis-band { fill: rgba(0,0,0,0.82); }
  .mechanostasis-text { fill: var(--ink-light); font-size: 22px; font-weight: 600; text-anchor: middle; }
  .link-line { stroke: var(--ink-light); stroke-width: 3; fill: none; }
  .forces-band { fill: var(--forces-band); }
  .forces-text { fill: var(--ink-light); font-size: 26px; font-weight: 600; }
  .fitness-box { fill: var(--fitness); }
  .fitness-low { fill: var(--fitness-low); }
  .frailty-box { fill: var(--frailty); }
  .frailty-low { fill: var(--frailty-low); }
  .box-divider { stroke: rgba(0,0,0,0.15); stroke-width: 2; }
  .box-head { fill: var(--ink-light); font-size: 27px; font-weight: 600; text-anchor: middle; }
  .box-body { fill: var(--ink-light); font-size: 25px; font-weight: 600; text-anchor: middle; }
  .box-state { fill: var(--ink-light); font-size: 30px; font-weight: 600; text-anchor: middle; }
  .step-body { fill: var(--step); }
  .step-top { fill: var(--step-top); }
  .step-text { fill: var(--ink-step); font-size: 19px; font-weight: 600; text-anchor: middle; }
</style>
</head>
<body>
<svg class="concept-sheet" viewBox="0 0 1500 1500" xmlns="http://www.w3.org/2000/svg">
  <defs>
    <radialGradient id="cellViewColour" cx="50%" cy="50%" r="50%">
      <stop offset="0" stop-color="#2f6b2a"/>
      <stop offset="0.7" stop-color="#1f4a1c"/>
      <stop offset="1" stop-color="#0a160a"/>
    </radialGradient>
    <radialGradient id="cellViewMono" cx="50%" cy="50%" r="50%">
      <stop offset="0" stop-color="#5a5a5a"/>
      <stop offset="0.7" stop-color="#3a3a3a"/>
      <stop offset="1" stop-color="#121212"/>
    </radialGradient>

    <g id="conceptPanel">
      <rect class="panel-bg" x="97" y="8" width="1306" height="735"/>
      <text class="title" x="750" y="86">Vorlint Concept and Envisioned Project Progression</text>

      <!-- forces -->
      <path class="force-wedge" d="M520,348 A230,230 0 0 1 581.8,191.1 L654.9,259.3 A130,130 0 0 0 620,348 Z"/>
      <path class="force-wedge" d="M593.1,179.9 A230,230 0 0 1 742,118.1 L745.5,218.1 A130,130 0 0 0 661.3,253 Z"/>
      <path class="force-wedge" d="M758,118.1 A230,230 0 0 1 906.9,179.9 L838.7,253 A130,130 0 0 0 754.5,218.1 Z"/>
      <path class="force-wedge" d="M918.2,191.1 A230,230 0 0 1 980,348 L880,348 A130,130 0 0 0 845.1,259.3 Z"/>

      <rect class="force-icon" role="img" aria-label="Cell squeezed by pressure" x="535" y="255" width="80" height="75" rx="10"/>
      <rect class="force-icon" role="img" aria-label="Cell pushed by shear flow" x="612" y="160" width="95" height="45" rx="10"/>
      <rect class="force-icon" role="img" aria-label="Cell pulled by tension" x="780" y="155" width="85" height="50" rx="10"/>
      <rect class="force-icon" role="img" aria-label="Cell stretched by strain" x="870" y="250" width="90" height="85" rx="10"/>

      <text class="force-label" transform="translate(528,270) rotate(-62)">Pressure</text>
      <text class="force-label" transform="translate(655,137) rotate(-20)">Shear</text>
      <text class="force-label" transform="translate(846,140) rotate(22)">Tension</text>
      <text class="force-label" transform="translate(963,258) rotate(68)">Strain</text>

      <circle class="cell-view" role="img" aria-label="Microscopy view of stained cells" cx="750" cy="345" r="135"/>

      <polygon class="pointer" points="700,227 686,236 699,242"/>
      <polygon class="pointer" points="794,226 808,234 796,241"/>
      <polygon class="pointer" points="619,298 633,303 622,312"/>
      <polygon class="pointer" points="878,294 866,302 878,310"/>

      <!-- mechanostasis -->
      <rect class="mechanostasis-band" x="650" y="372" width="200" height="36"/>
      <text class="mechanostasis-text" x="752" y="397">Mechanostasis</text>
      <line class="link-line" x1="648" y1="389" x2="612" y2="389"/>
      <polygon class="pointer" points="601,389 616,381 616,397"/>
      <line class="link-line" x1="898" y1="389" x2="935" y2="389"/>
      <line class="link-line" x1="898" y1="380" x2="898" y2="398"/>

      <!-- forces tag -->
      <rect class="forces-band" x="1072" y="176" width="331" height="53"/>
      <polygon class="pointer" points="1087,200 1113,186 1113,214"/>
      <text class="forces-text" x="1139" y="213">Forces on cells</text>

      <!-- health -->
      <rect class="fitness-box" x="201" y="358" width="262" height="252" rx="4"/>
      <path class="fitness-low" d="M201,540 Q332,520 463,540 V606 a4,4 0 0 1 -4,4 H205 a4,4 0 0 1 -4,-4 Z"/>
      <line class="box-divider" x1="215" y1="427" x2="449" y2="427"/>
      <polygon class="pointer" points="448,389 462,381 462,397"/>
      <text class="box-head" x="332" y="400">Cell fitness</text>
      <text class="box-body" x="332" y="471">Functional</text>
      <text class="box-body" x="332" y="506">cellular machineries</text>
      <text class="box-state" x="332" y="581">Health</text>

      <!-- disease -->
      <rect class="frailty-box" x="1036" y="358" width="263" height="252" rx="4"/>
      <path class="frailty-low" d="M1036,540 Q1167,520 1299,540 V606 a4,4 0 0 1 -4,4 H1040 a4,4 0 0 1 -4,-4 Z"/>
      <line class="box-divider" x1="1050" y1="427" x2="1285" y2="427"/>
      <line class="link-line" x1="1036" y1="389" x2="1054" y2="389"/>
      <text class="box-head" x="1167" y="398">Cell frailty</text>
      <text class="box-body" x="1167" y="471">Dysfunctional</text>
      <text class="box-body" x="1167" y="506">cellular machineries</text>
      <text class="box-state" x="1167" y="578">Disease</text>

      <!-- project steps -->
      <g class="project-steps">
        <path class="step-body" d="M563,677 V707 A187,9 0 0 0 937,707 V677 Z"/>
        <ellipse class="step-top" cx="750" cy="677" rx="187" ry="9"/>
        <text class="step-text" x="750" y="705">Mechanical force models</text>

        <path class="step-body" d="M584,637 V663 A166,9 0 0 0 916,663 V637 Z"/>
        <ellipse class="step-top" cx="750" cy="637" rx="166" ry="9"/>
        <text class="step-text" x="750" y="658">Cell, tissue&amp; organ responses</text>

        <path class="step-body" d="M602,594 V619 A148,9 0 0 0 898,619 V594 Z"/>
        <ellipse class="step-top" cx="750" cy="594" rx="148" ry="9"/>
        <text class="step-text" x="750" y="615">Disease models</text>

        <path class="step-body" d="M621,554 V576 A129,9 0 0 0 879,576 V554 Z"/>
        <ellipse class="step-top" cx="750" cy="554" rx="129" ry="9"/>
        <text class="step-text" x="750" y="573">Cellular machineries</text>

        <path class="step-body" d="M640,519 V536 A110,9 0 0 0 860,536 V519 Z"/>
        <ellipse class="step-top" cx="750" cy="519" rx="110" ry="9"/>
        <text class="step-text" x="750" y="535">Critical targets</text>

        <path class="step-body" d="M657,486 V500 A93,9 0 0 0 843,500 V486 Z"/>
        <ellipse class="step-top" cx="750" cy="486" rx="93" ry="9"/>
        <text class="step-text" x="748" y="502">Prevention</text>

        <path class="step-body" d="M680,453 V467 A70,9 0 0 0 820,467 V453 Z"/>
        <ellipse class="step-top" cx="750" cy="453" rx="70" ry="9"/>
        <text class="step-text" x="750" y="469">Therapies</text>
      </g>
    </g>
  </defs>

  <rect x="0" y="0" width="1500" height="1500" fill="var(--page)"/>
  <use href="#conceptPanel" class="theme-colour"/>
  <use href="#conceptPanel" class="theme-mono" transform="translate(0,749)"/>
</svg>
</body>
</html>
```